Financial Retirement Seminar Mailer

We would like to redesign our mailer flyer so that it looks classier and more effective in attracting people to sign up for our events. We help people who are near or in retirement achieve their financial goals.

PLEASE CHANGE THE ENTIRE FORMAT OF THE FLYER AND DO NOT LET IT LOOK SIMILAR TO WHAT WE CURRENTLY HAVE. NOTHING HAS TO STAY THE SAME. THE MORE UNIQUE YOU ARE THE HIGHER YOUR CHANCES OF WINNING.
ALL IMAGES CAN BE CHANGED (except Dorian Feld's photo and the logo for Marlow's Hearth Restaurant)

Target Market(s)

Our Target Market are upper middle class adults nearing or in retirement ages 55+.

Industry/Entity Type

Finance

Font styles to use
Serif
Sans Serif

Colors
0255a3
fece3e
ffffff

Requirements
Must have
• -Must have a photo of Dorian Feld and logo of Marlows Hearth. All other images can be changed.
• -Use our company colors which are navy and GOLD (Please use gold gradients instead of just yellow color)
• -The flyer must be folded in half. The inside can be full page.
Nice to have
• -If you could make the gold color stand out somehow maybe a gradient gold.

```html
<!DOCTYPE html>
<html lang="en">
<head>
<meta charset="utf-8">
<title>Complimentary Dining and Retirement Education Mailer</title>
<link href="https://fonts.googleapis.com/css2?family=Cinzel:wght@500;700;900&family=EB+Garamond:wght@400;600;700&display=swap" rel="stylesheet">
<style>
:root{
  --navy:#1c2d5e;
  --navy-deep:#15234b;
  --gold:#fece3e;
  --gold-dark:#d9a520;
  --gold-grad:linear-gradient(100deg,#c9951c 0%,#fece3e 45%,#ffe27a 65%,#d6a324 100%);
  --white:#ffffff;
  --ink:#2a2f45;
  --stage:#a9abad;
}
*{box-sizing:border-box;margin:0;padding:0}
html,body{width:931px;height:1200px;overflow:hidden}
body{background:var(--stage);font-family:"EB Garamond",Georgia,serif;color:var(--ink);position:relative}
.spread{position:absolute;left:85px;width:760px;height:570px;overflow:hidden;box-shadow:0 10px 24px rgba(0,0,0,.25)}
.spread--outside{top:20px;background:var(--navy)}
.spread--inside{top:610px;background:var(--white)}
.fold{position:absolute;left:380px;top:0;width:1px;height:100%;background:rgba(0,0,0,.12)}
.abs{position:absolute}

/* outside */
.video-ring{left:28px;top:74px;width:108px;height:108px}
.video-cta{left:30px;top:190px;width:138px;font-family:"Cinzel",serif;color:#dfe3ef;font-size:13.5px;line-height:20px;font-weight:500}
.video-url{left:30px;top:256px;font-family:"Cinzel",serif;color:var(--gold);font-size:8.6px;font-weight:700;letter-spacing:.1px}
.venue-name{left:28px;top:395px;width:132px;height:62px;border:2px solid var(--white);border-radius:10px;display:flex;align-items:center;justify-content:center;text-align:center;font-family:"Cinzel",serif;font-weight:700;color:var(--white);font-size:14px;line-height:16px}
.venue-address{left:28px;top:466px;display:flex;gap:8px;color:var(--white);font-size:9.5px;line-height:12px;font-weight:600}
.register{left:24px;top:522px;color:var(--white);font-size:9.5px}
.register .label{font-family:"Cinzel",serif;color:var(--gold);font-weight:700;font-size:9.5px;margin-bottom:5px}
.register .row{display:flex;align-items:center;gap:6px;margin-bottom:5px;font-family:"Cinzel",serif;font-size:9px;font-weight:600}
.dot{width:12px;height:12px;border-radius:50%;background:var(--gold-grad);display:flex;align-items:center;justify-content:center}
.cover-photo{left:173px;top:84px;width:587px;height:426px;background:radial-gradient(circle at 68% 45%,#e3a15b 0%,#cf7b45 18%,#efe3cf 38%,#dcdcdf 60%,#c9c9cc 100%)}
.cover-title{left:390px;top:300px;width:360px;text-align:center;font-family:"Cinzel",serif;font-weight:900;font-size:27px;line-height:33px;color:var(--navy);text-shadow:0 0 2px #fff,0 0 6px rgba(255,255,255,.8)}
.cover-byline{left:390px;top:488px;width:360px;text-align:center;font-size:10.5px;color:var(--navy)}
.cover-logo{left:655px;top:32px;width:76px;height:38px;border:1.5px solid var(--white);border-radius:6px;display:flex;align-items:center;justify-content:center;text-align:center;font-family:"Cinzel",serif;font-weight:700;color:var(--white);font-size:8.5px;line-height:10px}
.urgency{left:390px;top:520px;width:360px;text-align:center;font-family:"Cinzel",serif;font-weight:700;color:var(--gold);font-size:11.5px;line-height:16px}

/* inside */
.ribbon{position:absolute;background:var(--gold-grad);clip-path:polygon(0 0,88% 0,100% 100%,0 100%);font-family:"Cinzel",serif;font-weight:700;color:var(--navy);display:flex;align-items:center}
.ribbon--host{left:0;top:28px;width:290px;height:26px;padding-left:20px;font-size:15px}
.ribbon--solutions{left:380px;top:28px;width:330px;height:48px;padding-left:18px;font-size:15px;line-height:17px}
.ribbon--topics{left:0;top:380px;width:215px;height:24px;padding-left:20px;font-size:15px}
.host-photo{left:25px;top:64px;width:124px;height:124px;border-radius:50%;border:2px solid var(--navy);background:radial-gradient(circle at 50% 40%,#f2f2f4 0%,#d8dbe2 55%,#2a3352 100%)}
.host-name{left:0;top:196px;width:175px;text-align:center;font-size:17px;color:var(--navy)}
.host-creds{left:0;top:218px;width:175px;text-align:center;font-size:6.6px;line-height:7.4px;color:var(--ink)}
.host-bio{left:170px;top:66px;width:205px;font-size:9px;line-height:11.4px;color:var(--ink)}
.host-bio b{font-weight:700;color:#111}
.featured{left:35px;top:290px;font-size:9.5px;font-weight:600;color:#111}
.badges{left:35px;top:310px;display:flex;gap:14px;align-items:center}
.badge{height:22px;background:var(--navy);border-radius:3px}
.solutions-lead{left:395px;top:86px;font-size:11px;color:var(--ink)}
.solutions-copy{left:395px;top:104px;width:325px;font-size:8.2px;line-height:10.2px;color:var(--ink)}
.no-selling{left:395px;top:168px;font-size:8.8px;font-weight:700;color:#111}
.enroll{left:395px;top:196px;width:332px;height:58px;background:var(--navy);text-align:center;color:var(--white);padding-top:9px}
.enroll .big{font-family:"Cinzel",serif;font-weight:700;font-size:16.5px}
.enroll .small{font-size:10px;margin-top:2px}
.dates{left:395px;top:282px;width:332px;text-align:center;font-size:10.5px;line-height:20px;color:var(--ink)}
.dates b{font-weight:700;color:#111}
.dates .time{background:var(--gold-grad);font-weight:700;color:var(--navy);padding:0 4px;font-family:"Cinzel",serif}
.topics-band{left:0;top:348px;width:760px;height:222px;background:var(--navy)}
.topic{position:absolute;top:412px;color:var(--white)}
.topic svg{display:block;width:48px;height:52px}
.topic h3{font-family:"Cinzel",serif;font-weight:700;font-size:11.5px;margin-top:12px;letter-spacing:.2px;white-space:nowrap}
.topic p{font-size:7.6px;line-height:9.4px;color:#c9cfe0;margin-top:4px}
.menu{left:0;top:544px;width:760px;text-align:center;color:var(--white);font-size:10.5px;font-weight:600}
</style>
</head>
<body>

<section class="spread spread--outside" aria-label="Mailer outside">
  <svg class="abs video-ring" viewBox="0 0 108 108" aria-hidden="true">
    <circle cx="54" cy="54" r="51" fill="none" stroke="#3a4a7a" stroke-width="3"/>
    <path d="M40 32 L76 54 L40 76 Z" fill="none" stroke="#3a4a7a" stroke-width="3" stroke-linejoin="round"/>
  </svg>
  <p class="abs video-cta">VIEW A VIDEO OF<br>DORIAN ONLINE<br>AND REGISTER AT</p>
  <p class="abs video-url">HEARTHSIDECLASSES.ORG</p>

  <div class="abs venue-name">MARLOW'S<br>HEARTH</div>
  <div class="abs venue-address">
    <span class="dot"><svg width="7" height="8" viewBox="0 0 7 8"><path d="M3.5 0a3 3 0 0 0-3 3c0 2 3 5 3 5s3-3 3-5a3 3 0 0 0-3-3z" fill="#1c2d5e"/></svg></span>
    <span>2410 Harbor Crest Ave. #230<br>Bayview Cove,<br>CA 90000 (Floor 2)</span>
  </div>
  <div class="abs register">
    <p class="label">REGISTER ONLINE OR CALL AT</p>
    <p class="row"><span class="dot"><svg width="8" height="8" viewBox="0 0 8 8"><circle cx="4" cy="4" r="3.2" fill="none" stroke="#1c2d5e" stroke-width=".9"/><path d="M.8 4h6.4M4 .8c-1.6 2-1.6 4.4 0 6.4M4 .8c1.6 2 1.6 4.4 0 6.4" fill="none" stroke="#1c2d5e" stroke-width=".7"/></svg></span>HEARTHSIDECLASSES.ORG</p>
    <p class="row"><span class="dot"><svg width="7" height="7" viewBox="0 0 7 7"><path d="M1.2 .5l1.3 1.6-.6.9c.4.9 1.2 1.7 2.1 2.1l.9-.6 1.6 1.3-.8 1C3.6 6.5.5 3.4.2 1.3z" fill="#1c2d5e"/></svg></span>888-555-0143</p>
  </div>

  <div class="abs cover-photo" role="img" aria-label="Overhead photo of a seafood pasta bowl with mussels, clams and a lemon wedge on a linen napkin"></div>
  <h1 class="abs cover-title">COMPLIMENTARY<br>DINING<br>AND<br>RETIREMENT<br>EDUCATION</h1>
  <p class="abs cover-byline">By: Westbrook College Instructor Dorian Feld</p>
  <div class="abs cover-logo">MARLOW'S<br>HEARTH</div>
  <p class="abs urgency">REGISTRATION IS LIMITED!<br>CONFIRM TODAY</p>
  <div class="fold"></div>
</section>

<section class="spread spread--inside" aria-label="Mailer inside">
  <h2 class="ribbon ribbon--host">MEET YOUR HOST</h2>
  <div class="abs host-photo" role="img" aria-label="Portrait photo of host Dorian Feld"></div>
  <p class="abs host-name">Dorian Feld</p>
  <p class="abs host-creds">Certified Financial Planner<br>Instructor at Westbrook College<br>Daily Ledger Writer</p>
  <p class="abs host-bio">Dorian Feld is a <b>Certified Financial Planner,</b> financial <b>writer for the Daily Ledger,</b> instructor at <b>Westbrook College,</b> and pioneer in the field of <b>Financial Therapy</b> and <b>Conscious Wealth Building for Retirement.</b><br>Dorian's understanding of the connection between emotional and financial well being is the catalyst that empowers his clients to take positive action toward improving the quality of their lives and finances for retirement. He works with individuals and families to create wealth, legacy and impact. A regular speaker on KWR 990AM and a frequent guest on popular financial shows. Dorian's firm, Stillwater Financial exclusively works with people ages 55-67 years old who are in retirement or focused on retiring.</p>
  <p class="abs featured">Dorian has been featured in the following and more:</p>
  <div class="abs badges" aria-label="Media features">
    <span class="badge" style="width:36px"></span>
    <span class="badge" style="width:50px"></span>
    <span class="badge" style="width:44px"></span>
    <span class="badge" style="width:44px"></span>
    <span class="badge" style="width:22px;border-radius:50%"></span>
  </div>

  <h2 class="ribbon ribbon--solutions">ADVANCED RETIREMENT<br>SOLUTIONS</h2>
  <p class="abs solutions-lead">Featuring Westbrook College Instructor Dorian Feld, CFP</p>
  <p class="abs solutions-copy">You are invited to an educational talk featuring Westbrook College Instructor Dorian Feld. This free* event is focused on teaching the techniques and tools that your financial advisor does not want you to know. Instructor Dorian Feld will cover advanced retirement and tax topics which are proven to be successful and mostly unknown to consumers.</p>
  <p class="abs no-selling">Leave your checkbooks at home, there will be no selling here!</p>
  <div class="abs enroll">
    <p class="big">EARLY ENROLLMENT IS FREE.</p>
    <p class="small">Participants may enroll at door for <b>$99</b> per seat.</p>
  </div>
  <p class="abs dates">TUESDAY &nbsp;<b>OCTOBER 8<sup>th</sup></b> <span class="time">AT 7:00 PM</span><br>WEDNESDAY &nbsp;<b>OCTOBER 9<sup>th</sup></b> <span class="time">AT 7:00 PM</span></p>

  <div class="abs topics-band"></div>
  <h2 class="ribbon ribbon--topics">TOPICS</h2>

  <article class="topic" style="left:19px;width:165px">
    <svg viewBox="0 0 48 52" aria-hidden="true"><path d="M24 1 46 13.5v25L24 51 2 38.5v-25z" fill="#fff"/><circle cx="16" cy="26" r="6" fill="none" stroke="#1c2d5e" stroke-width="2"/><circle cx="32" cy="26" r="6" fill="none" stroke="#1c2d5e" stroke-width="2"/><path d="M12 14a15 15 0 0 1 24 0M36 38a15 15 0 0 1-24 0" fill="none" stroke="#1c2d5e" stroke-width="1.6"/></svg>
    <h3>LOW-RISK INVESTING</h3>
    <p>New low-risk investments that produce 5%-7% interest and can provide you long term care income. (Not Stocks/Bonds)</p>
  </article>
  <article class="topic" style="left:209px;width:165px">
    <svg viewBox="0 0 48 52" aria-hidden="true"><path d="M24 1 46 13.5v25L24 51 2 38.5v-25z" fill="#fff"/><path d="M22 22l8-7 8 7v8H22z" fill="none" stroke="#1c2d5e" stroke-width="2"/><circle cx="13" cy="31" r="3" fill="#1c2d5e"/><path d="M9 40h8M20 38h16" stroke="#1c2d5e" stroke-width="2"/></svg>
    <h3>ESTATE PLANNING</h3>
    <p>If you own a home, it's essential to have a Trust in order to avoid probate and to protect yourself if you become disabled.</p>
  </article>
  <article class="topic" style="left:406px;width:140px">
    <svg viewBox="0 0 48 52" aria-hidden="true"><path d="M24 1 46 13.5v25L24 51 2 38.5v-25z" fill="#fff"/><rect x="14" y="13" width="20" height="26" fill="none" stroke="#1c2d5e" stroke-width="2"/><path d="M18 21h12M18 26h12M18 31h8" stroke="#1c2d5e" stroke-width="1.6"/></svg>
    <h3>TAX STRATEGIES</h3>
    <p>Learn how to save at least 30% on your 401k taxes and greatly reduce your taxable income in retirement.</p>
  </article>
  <article class="topic" style="left:566px;width:175px">
    <svg viewBox="0 0 48 52" aria-hidden="true"><path d="M24 1 46 13.5v25L24 51 2 38.5v-25z" fill="#fff"/><circle cx="18" cy="16" r="3.5" fill="#1c2d5e"/><circle cx="30" cy="16" r="3.5" fill="#1c2d5e"/><rect x="14" y="21" width="8" height="18" rx="2" fill="#1c2d5e"/><rect x="26" y="21" width="8" height="18" rx="2" fill="#1c2d5e"/></svg>
    <h3>LONG TERM CARE</h3>
    <p>Learn how to protect yourself against the high costs of long-term care. Discover 3 new solutions you may not have seen before.</p>
  </article>

  <p class="abs menu">Choose From: Vegan, Vegetarian, Seafood, Pasta or Steak</p>
  <div class="fold"></div>
</section>

</body>
</html>
```